Lena Hartwell Web

Lena Hartwell is a singer/songwriter that has a presence in the market for over 20 years. She currently has a website, lenahartwell.example that needs a major makeover. IT needs to be reorganized to; 1) make it more user friendly; 2) enable multi-languages including; Spanish, French, Russian, Japanese, Chinese and Portuguese; 3) enable purchases online through a storefront of promotional merchandise and music tracks. She has a logo that needs an update, as well as we currently have a business card open on PixelBazaar for input. Working to re-brand, or refresh her brand.

Lena Hartwell is the next Rosa Delmont! She has 5 platinum records, Lumen Award nominations and tours with Harold Prescott globally and is Nora Vandermeer's key backup singer for 12 years.
Updates

Some common questions have come up.  Here is some further input:

1) Colors - No specific color in mind but probably earth tones.  Although at this point we''re completely open.  Mary likes classical style, Russian, French decor.  Paris architecture. Greek, Italian textures, Goddess like symbols from the Roman Empire, or the symbols and pomp of the British monarchy.  One name on tap for the new CD is "Lanterns Over Quiet Water"
2) Example website - I have not found a new one specifically, but what I don''t like about the existing one is it is not easy to navigate.  Needs to be streamlined and easy to navigate with a storefront for merchandise and music downloads.  
3) On Logo - We''re revamping a "Global" merchandise rollout logo.  We''ve also considered possibly modifying the old english "Hartwell" family crest which signifies royalty, but have not explored that too much.  The hexagon yellow logo on her current website, I was thinking of modifying to gold (brushed - or polished?), then taking the LH lettering using a fountain pen type look there the line thickness flows with pressure on the pen, then make the gold look like a pillow, with the letter making an impression into the gold pillow.  This expands to a high quality pin, blinged up broach with diamonds imbedded for example, Global label identity, tee shirts, label tag on fashion clothing etc etc. 
 4) One thing marketing has asked us to build is a routine video blog to reach out to fans in a personal way.  Short clips of daily activity, travel prep for shows, etc. Possibly a signup/fanpage where people get emails sent back whenever anything new is posted, like a video blog, new pics, new events.  A menu to choose what you get updates on. 

Thanks, Dennis

Target Market(s)

1) Fan base in Europe, Asia, Latin America and North America
2) Movie producers seeking soundtracks
3) Private clients seeking an outstanding performer for corporate events

Industry/Entity Type

Singer

Requirements
Must have
• Better organization into smaller pages. Items critical include: 1) music tracks, 2) ClipStream links, 3) photos & Video, 4) storefront to enable online merchandise purchase 5) a way to illustrate her genre from; gospel, to rock, funk, R&B, country,

```html
<!DOCTYPE html>
<html lang="en">
<head>
<meta charset="utf-8">
<title>Lena Hartwell — Home</title>
<link rel="stylesheet" href="https://fonts.googleapis.com/css2?family=Cinzel:wght@500;700&family=Great+Vibes&family=Oswald:wght@400;500;600&display=swap">
<style>
  :root {
    --ink: #0c0907;
    --night: #16100b;
    --umber: #3a2817;
    --bronze: #7a5632;
    --amber: #e7a868;
    --amber-deep: #c9844a;
    --gold: #f0c419;
    --cream: #f4ece1;
    --muted: #8a7b6c;
    --band: rgba(8, 6, 4, 0.88);
  }
  * { box-sizing: border-box; margin: 0; padding: 0; }
  html, body { width: 1200px; height: 900px; overflow: hidden; background: var(--ink); }
  .site {
    position: relative;
    width: 1200px;
    height: 900px;
    overflow: hidden;
    font-family: "Oswald", sans-serif;
    color: var(--cream);
    background: var(--night);
  }
  .hero-photo {
    position: absolute;
    inset: 0 0 130px 0;
    background:
      radial-gradient(ellipse 300px 380px at 900px 330px, rgba(140, 100, 60, 0.55), transparent 70%),
      radial-gradient(ellipse 380px 260px at 300px 360px, rgba(110, 78, 45, 0.5), transparent 70%),
      radial-gradient(circle 3px at 680px 250px, rgba(255,240,210,.8), transparent),
      radial-gradient(circle 4px at 760px 220px, rgba(255,240,210,.7), transparent),
      radial-gradient(circle 3px at 840px 280px, rgba(255,240,210,.7), transparent),
      radial-gradient(circle 3px at 1050px 240px, rgba(255,240,210,.6), transparent),
      radial-gradient(circle 4px at 620px 320px, rgba(255,240,210,.6), transparent),
      linear-gradient(160deg, #2b1d11 0%, #4a331d 40%, #241810 75%, #120c08 100%);
  }
  .top-stripe {
    position: absolute;
    left: 0; top: 98px;
    width: 340px; height: 8px;
    background: var(--amber);
    clip-path: polygon(0 0, 100% 0, 97% 100%, 0 100%);
  }
  .top-shade {
    position: absolute;
    left: 0; top: 106px;
    width: 1200px; height: 120px;
    background: linear-gradient(to bottom, rgba(0,0,0,.55), transparent);
    clip-path: polygon(0 0, 340px 0, 1200px 0, 1200px 100%, 0 100%);
  }
  .main-nav {
    position: absolute;
    top: 0; right: 0;
    width: 720px; height: 66px;
    background: var(--band);
    clip-path: polygon(40px 0, 100% 0, 100% 100%, 0 100%);
    display: flex;
    align-items: center;
    gap: 58px;
    padding-left: 90px;
  }
  .main-nav a {
    position: relative;
    color: var(--cream);
    text-decoration: none;
    font-size: 15px;
    font-weight: 500;
    letter-spacing: 1.5px;
  }
  .main-nav a.is-current { color: var(--amber); }
  .main-nav a.is-current::after {
    content: "";
    position: absolute;
    left: 0; right: 0; bottom: -8px;
    height: 3px;
    background: var(--amber);
  }
  .language-select {
    position: absolute;
    top: 78px; left: 690px;
    width: 260px; height: 28px;
    border: 1px solid rgba(244,236,225,.25);
    background: rgba(0,0,0,.6);
    display: flex; align-items: center; justify-content: space-between;
    padding: 0 12px;
    font-size: 12px; letter-spacing: 1.5px; color: var(--muted);
  }
  .brand {
    position: absolute;
    top: 150px; left: 58px;
    display: flex; align-items: center; gap: 14px;
  }
  .brand-mark { width: 40px; height: 40px; background: var(--gold); }
  .brand-name {
    font-family: "Cinzel", serif;
    font-weight: 500;
    font-size: 25px;
    color: var(--cream);
    letter-spacing: 1px;
  }
  .release {
    position: absolute;
    left: 80px; top: 400px;
    width: 500px;
  }
  .release-title {
    display: block;
    padding: 12px 30px 14px 34px;
    background: var(--band);
    clip-path: polygon(0 18%, 100% 0, 97% 100%, 3% 100%);
    font-family: "Great Vibes", cursive;
    font-weight: 400;
    font-size: 38px;
    color: var(--cream);
    white-space: nowrap;
  }
  .release-tagline {
    margin: 8px 0 0 34px;
    font-size: 12px;
    letter-spacing: 5px;
    color: var(--cream);
  }
  .release-actions { position: relative; height: 90px; }
  .btn {
    position: absolute;
    display: flex; align-items: center; justify-content: center; gap: 10px;
    height: 50px;
    background: var(--amber);
    color: var(--ink);
    font-size: 19px; font-weight: 600; letter-spacing: 1.5px;
    text-decoration: none;
    clip-path: polygon(4% 0, 100% 0, 96% 100%, 0 100%);
  }
  .btn svg { width: 18px; height: 18px; fill: var(--ink); }
  .btn-login { left: 30px; top: 30px; width: 220px; }
  .btn-buy { left: 262px; top: 4px; width: 210px; background: var(--amber-deep); }
  .media-tray {
    position: absolute;
    left: 430px; top: 560px;
    width: 770px; height: 180px;
    background: rgba(20,14,9,.92);
    clip-path: polygon(0 10%, 100% 0, 100% 100%, 20% 100%);
  }
  .media-links {
    position: absolute;
    left: 560px; top: 590px;
    display: flex; gap: 18px;
  }
  .media-tile {
    position: relative;
    width: 190px; height: 110px;
    border: 3px solid #1a120c;
    text-decoration: none;
  }
  .media-tile.is-partial { width: 110px; }
  .media-tile .tile-photo { position: absolute; inset: 0; }
  .tile-gallery { background: linear-gradient(135deg, #d9d4cc, #4a4744 60%, #1b1a19); }
  .tile-videos { background: radial-gradient(circle at 60% 40%, #f58c6a, #b63a9a 45%, #3a2a9c); }
  .tile-more { background: linear-gradient(135deg, #f3e6da, #b89a86 50%, #2a211c); }
  .media-label {
    position: absolute;
    right: 10px; bottom: 6px;
    color: #fff;
    font-size: 15px; font-weight: 600; letter-spacing: 1px;
  }
  .lower-band {
    position: absolute;
    left: 0; top: 740px;
    width: 1200px; height: 70px;
    background: var(--ink);
    clip-path: polygon(0 0, 58% 0, 54% 100%, 0 100%);
  }
  .slider-arrows {
    position: absolute;
    left: 100px; top: 752px;
    display: flex; gap: 4px;
  }
  .slider-arrows span {
    width: 26px; height: 26px;
    background: #2a1f16;
    display: flex; align-items: center; justify-content: center;
  }
  .slider-arrows svg { width: 10px; height: 10px; fill: var(--cream); }
  .site-footer {
    position: absolute;
    left: 100px; top: 820px;
    font-size: 11px; letter-spacing: .5px;
    color: var(--muted);
  }
</style>
</head>
<body>
<div class="site">
  <div class="hero-photo" role="img" aria-label="Warm sepia concert photograph of the singer performing on stage with a band and bokeh stage lights"></div>
  <div class="top-shade"></div>
  <div class="top-stripe"></div>

  <nav class="main-nav">
    <a href="#" class="is-current">HOME</a>
    <a href="#">STORE</a>
    <a href="#">BLOG</a>
    <a href="#">ABOUT</a>
    <a href="#">CONTACT</a>
  </nav>

  <div class="language-select">
    <span>ENGLISH</span>
    <svg width="10" height="6" viewBox="0 0 10 6"><path d="M0 0h10L5 6z" fill="#8a7b6c"/></svg>
  </div>

  <div class="brand">
    <span class="brand-mark"></span>
    <span class="brand-name">Lena Hartwell</span>
  </div>

  <section class="release">
    <h1 class="release-title">Lanterns Over Quiet Water</h1>
    <p class="release-tagline">IN STORES ONLINE COLLECT NOW</p>
    <div class="release-actions">
      <a href="#" class="btn btn-login">LOGIN
        <svg viewBox="0 0 16 16"><circle cx="8" cy="5" r="3.5"/><path d="M1 16c0-4 3-6.5 7-6.5s7 2.5 7 6.5z"/></svg>
      </a>
      <a href="#" class="btn btn-buy">BUY NOW
        <svg viewBox="0 0 16 16"><path d="M0 5h16l-2 10H2z M4 5l3-5 1 .6L5.3 5z M12 5L9 0 8 .6 10.7 5z"/></svg>
      </a>
    </div>
  </section>

  <div class="media-tray"></div>
  <div class="media-links">
    <a href="#" class="media-tile">
      <span class="tile-photo tile-gallery" role="img" aria-label="Black and white photo of the singer on stage"></span>
      <span class="media-label">GALLERY</span>
    </a>
    <a href="#" class="media-tile">
      <span class="tile-photo tile-videos" role="img" aria-label="Colourful stage photo of the singer with a microphone"></span>
      <span class="media-label">VIDEOS</span>
    </a>
    <a href="#" class="media-tile is-partial">
      <span class="tile-photo tile-more" role="img" aria-label="Portrait photo of the singer"></span>
    </a>
  </div>

  <div class="lower-band"></div>
  <div class="slider-arrows">
    <span><svg viewBox="0 0 10 10"><path d="M7 0v10L1 5z"/></svg></span>
    <span><svg viewBox="0 0 10 10"><path d="M3 0v10l6-5z"/></svg></span>
  </div>

  <footer class="site-footer">Copyright 2014 Lena Hartwell. All rights reserved.</footer>
</div>
</body>
</html>
```